business card and letter head for Australian company manufacturing rienforcing steel for constructio

business card and letter head using our logo. you will need to change the name of the logo to KOLVATIN and the red part of the logo needs to start at the e after d.

Architects, Engineers, Builders, Developers

Manufacturing

```html
<!DOCTYPE html>
<html lang="en">
<head>
<meta charset="utf-8">
<title>KOLVATIN – Letterhead and Business Card</title>
<link rel="stylesheet" href="https://fonts.googleapis.com/css2?family=Open+Sans:wght@400;700;800&family=Arimo:wght@400;700&display=swap">
<style>
  :root {
    --green: #5b8a2e;
    --green-light: #8ec04a;
    --green-dark: #4a7526;
    --sage: #c9d1b8;
    --ink: #3a2d29;
    --text: #666666;
    --label: #333333;
    --red: #b3261e;
    --paper: #ffffff;
  }
  * { margin: 0; padding: 0; box-sizing: border-box; }
  html, body { width: 848px; height: 1200px; overflow: hidden; background: var(--paper); }
  .sheet { position: relative; width: 848px; height: 1200px; background: var(--paper); }

  .band { position: absolute; left: 0; top: 0; display: block; }

  .brand {
    position: absolute;
    display: flex; align-items: center; gap: 6px;
    font-family: "Open Sans", sans-serif;
    font-weight: 800;
    color: var(--ink);
    letter-spacing: -0.3px;
    line-height: 1;
  }
  .brand-dot { border-radius: 50%; background: var(--ink); flex: none; }

  .letterhead .brand { left: 78px; top: 60px; font-size: 22px; }
  .letterhead .brand-dot { width: 16px; height: 16px; }

  .contact {
    position: absolute;
    font-family: "Arimo", sans-serif;
    font-style: normal;
    color: var(--text);
    text-align: right;
    line-height: 1.75;
    white-space: nowrap;
  }
  .contact b { color: var(--label); font-weight: 700; }
  .contact .email { color: var(--red); }

  .letterhead .contact { right: 20px; top: 80px; font-size: 7px; }

  .card { position: absolute; left: 50px; top: 770px; width: 484px; height: 290px; }
  .card .brand { left: 74px; top: 160px; font-size: 24px; }
  .card .brand-dot { width: 18px; height: 18px; }
  .card-name {
    position: absolute; right: 28px; top: 42px;
    font-family: "Open Sans", sans-serif; font-size: 15px; color: #222; text-align: right;
  }
  .card-role {
    position: absolute; right: 28px; top: 66px;
    font-family: "Open Sans", sans-serif; font-size: 13.5px; color: var(--red);
    letter-spacing: 0.6px; text-align: right;
  }
  .card .contact { right: 28px; top: 166px; font-size: 8.5px; }
</style>
</head>
<body>
<div class="sheet">

  <header class="letterhead">
    <svg class="band" width="848" height="152" viewBox="0 0 848 152" aria-hidden="true">
      <defs>
        <radialGradient id="lh-glow" cx="110" cy="72" r="260" gradientUnits="userSpaceOnUse">
          <stop offset="0" stop-color="#8ec04a"/>
          <stop offset="1" stop-color="#4a7526"/>
        </radialGradient>
      </defs>
      <rect x="0" y="0" width="848" height="3" fill="#5b8a2e"/>
      <polygon points="0,0 382,0 425,150 0,150" fill="url(#lh-glow)"/>
      <rect x="425" y="148" width="423" height="2" fill="#5b8a2e"/>
    </svg>
    <div class="brand"><span class="brand-dot"></span>kolvatin</div>
    <address class="contact">
      <b>Tel :</b> 013 0400 0120<br>
      <b>Mob :</b> 0890417226<br>
      <b>Email :</b> <span class="email">dean@kolvatin.com</span><br>
      <b>Web :</b> www.kolvatin.com<br>
      Harbour Lane, 12 Wattle Place, Geelong 3220
    </address>
  </header>

  <section class="card">
    <svg class="band" width="484" height="290" viewBox="0 0 484 290" aria-hidden="true">
      <defs>
        <radialGradient id="card-glow" cx="120" cy="150" r="240" gradientUnits="userSpaceOnUse">
          <stop offset="0" stop-color="#8ec04a"/>
          <stop offset="1" stop-color="#4a7526"/>
        </radialGradient>
      </defs>
      <rect x="0.5" y="0.5" width="483" height="289" fill="#ffffff" stroke="#e6e6e6"/>
      <rect x="0" y="0" width="191" height="8" fill="#c9d1b8"/>
      <rect x="191" y="0" width="293" height="6" fill="#5b8a2e"/>
      <polygon points="0,8 190,8 290,282 0,282" fill="url(#card-glow)"/>
      <rect x="0" y="282" width="291" height="8" fill="#c9d1b8"/>
      <rect x="291" y="283" width="193" height="7" fill="#5b8a2e"/>
    </svg>
    <div class="brand"><span class="brand-dot"></span>kolvatin</div>
    <div class="card-name">Dean Talbrook</div>
    <div class="card-role">Marketing Head</div>
    <address class="contact">
      <b>Tel :</b> 013 0400 0120<br>
      <b>Mob :</b> 0890417226<br>
      <b>Email :</b> <span class="email">dean@kolvatin.com</span><br>
      <b>Web :</b> www.kolvatin.com<br>
      Harbour Lane, 12 Wattle Place, Geelong 3220
    </address>
  </section>

</div>
</body>
</html>
```